Super Greens Label for Supplement Bottle

We want to design a front label for a health supplement bottle. The product is called Meadow Twist Chews™. This will be a new product so there is no current website for the product. The focus is on supergreens that taste great and deliver support for energy, digestion, and immune defense.
We want it to be modern, vibrant and appealing.
Bottle size: standard size supplement CLEAR bottle size, with white child resistant cap and the label panel dimensions are 3” x 7”. The label should be primarily white and green, with a touch of red; (see color palettes)/it can also ONLY be white and green. See samples attached.
We are only focused on the front of the bottle design, not on the back, but leave space for the supplement panel and other text on the back.
So the text for the front of the bottle is:
RT Balden's
Meadow Twist Chews™
Super Greens Blend for:
Energy, Digestion, and Immune Support*
60 Gummies | Dietary Supplement
Raspberry Flavor Gummies
Off to side of the label:
Non-GMO
Vegan Friendly
Plant-Based
Gelatin Free
Colors
Designer to choose colors to be used in the design.

```html
<!DOCTYPE html>
<html lang="en">
<head>
<meta charset="utf-8">
<title>Meadow Twist Chews – Front Label</title>
<link rel="stylesheet" href="https://fonts.googleapis.com/css2?family=Poppins:wght@400;500;700;800&family=Dosis:wght@600;700&display=swap">
<style>
  :root {
    --bg: #ffffff;
    --label-white: #f7f7f7;
    --green-mid: #3fae2a;
    --green-light: #8fd96a;
    --green-dark: #1e5123;
    --green-sage: #5e9c6b;
    --badge-green: #5cc043;
    --red: #c81a30;
    --red-pink: #e8657f;
    --ink: #333333;
  }
  * { box-sizing: border-box; margin: 0; padding: 0; }
  html, body { width: 1067px; height: 1200px; overflow: hidden; background: var(--bg); }
  .canvas { position: relative; width: 1067px; height: 1200px; background: var(--bg); }
  .label {
    position: absolute; left: 83px; top: 68px; width: 900px; height: 1064px;
    background: var(--label-white); overflow: hidden;
    font-family: "Poppins", sans-serif;
  }
  .label-bands { position: absolute; inset: 0; }
  .center-text { position: absolute; left: 375px; transform: translateX(-50%); text-align: center; white-space: nowrap; line-height: 1; }
  .product-name { top: 252px; font-size: 80px; font-weight: 800; letter-spacing: -2px; }
  .product-name .word-one { color: var(--green-sage); }
  .product-name .word-two { color: var(--green-dark); }
  .product-type { top: 382px; left: 362px; font-size: 82px; font-weight: 500; color: var(--green-light); }
  .blend-intro { top: 510px; font-size: 46px; font-weight: 400; color: var(--ink); letter-spacing: -0.5px; }
  .blend-rule { position: absolute; top: 578px; left: 86px; width: 582px; height: 3px; background: var(--green-mid); }
  .benefits-main { top: 604px; font-size: 57px; font-weight: 500; color: var(--ink); letter-spacing: -1px; }
  .benefits-sub { top: 678px; font-size: 49px; font-weight: 400; color: var(--ink); letter-spacing: -0.5px; }
  .count { position: absolute; top: 766px; left: 68px; font-size: 86px; font-weight: 700; line-height: 1; color: var(--red); white-space: nowrap; letter-spacing: -1px; }
  .count .count-num { color: var(--red-pink); }
  .flavor-art {
    position: absolute; left: 614px; top: 752px; width: 92px; height: 112px; border-radius: 48% 48% 50% 50%;
    background: radial-gradient(circle at 45% 40%, #f6c3cd, #e8657f 80%); opacity: .55;
  }
  .supplement-type { position: absolute; top: 864px; left: 68px; font-family: "Dosis", sans-serif; font-size: 66px; font-weight: 600; color: var(--green-mid); line-height: 1; white-space: nowrap; }
  .flavor-band-text { position: absolute; top: 972px; left: 30px; font-family: "Dosis", sans-serif; font-size: 58px; font-weight: 600; color: #ffffff; line-height: 1; white-space: nowrap; }
  .nongmo-text { position: absolute; left: 716px; top: 104px; width: 166px; text-align: center; font-size: 28px; font-weight: 500; color: #ffffff; line-height: 1; white-space: nowrap; }
  .claims { position: absolute; left: 726px; top: 0; width: 160px; height: 900px; text-align: center; font-family: "Dosis", sans-serif; color: var(--badge-green); }
  .claim-icon { position: absolute; left: 50%; transform: translateX(-50%); }
  .claim-text { position: absolute; left: 0; width: 160px; font-size: 35px; font-weight: 600; line-height: 1.22; }
  .icon-vegan { top: 240px; }
  .text-vegan { top: 324px; }
  .icon-plant { top: 442px; }
  .text-plant { top: 520px; }
  .icon-gelatin { top: 650px; }
  .text-gelatin { top: 710px; }
</style>
</head>
<body>
<div class="canvas">
  <div class="label">
    <svg class="label-bands" width="900" height="1064" viewBox="0 0 900 1064" aria-hidden="true">
      <defs>
        <linearGradient id="bandGrad" x1="0" x2="1" y1="0" y2="0">
          <stop offset="0" stop-color="#55c22b"/>
          <stop offset="0.35" stop-color="#a6e287"/>
          <stop offset="0.62" stop-color="#55c22b"/>
          <stop offset="1" stop-color="#3fa824"/>
        </linearGradient>
        <linearGradient id="badgeGrad" x1="0" x2="1" y1="0" y2="0">
          <stop offset="0" stop-color="#e8657f"/>
          <stop offset="1" stop-color="#c81a30"/>
        </linearGradient>
      </defs>
      <polygon points="0,0 900,0 900,72 354,72 311,157 0,157" fill="url(#bandGrad)"/>
      <rect x="0" y="946" width="900" height="106" fill="url(#bandGrad)"/>
      <rect x="0" y="1052" width="900" height="12" fill="#a6e287" opacity=".6"/>
      <polygon points="716,0 882,0 882,168 799,201 716,168" fill="url(#badgeGrad)"/>
    </svg>

    <div class="nongmo-text">Non-GMO</div>

    <div class="center-text product-name"><span class="word-one">MEADOW</span> <span class="word-two">TWIST</span></div>
    <div class="center-text product-type">CHEWS</div>
    <div class="center-text blend-intro">SUPER GREENS BLEND FOR</div>
    <div class="blend-rule"></div>
    <div class="center-text benefits-main">ENERGY, DIGESTION,</div>
    <div class="center-text benefits-sub">AND IMMUNE SUPPORT*</div>

    <div class="count"><span class="count-num">60</span> GUMMIES</div>
    <div class="flavor-art" role="img" aria-label="Raspberry line illustration"></div>
    <div class="supplement-type">DIETARY SUPPLEMENT</div>

    <div class="flavor-band-text">RASPBERRY FLAVOR GUMMIES</div>

    <div class="claims">
      <svg class="claim-icon icon-vegan" width="64" height="70" viewBox="0 0 64 70" role="img" aria-label="Carrot icon">
        <path d="M8 64 C6 58 30 30 40 24 C46 22 52 28 48 34 C42 44 14 66 8 64 Z" fill="none" stroke="#5cc043" stroke-width="3" stroke-linejoin="round"/>
        <path d="M44 24 L50 8 M47 26 L60 16 M49 29 L62 30" stroke="#5cc043" stroke-width="3" stroke-linecap="round"/>
      </svg>
      <div class="claim-text text-vegan">VEGAN<br>FRIENDLY</div>

      <svg class="claim-icon icon-plant" width="44" height="62" viewBox="0 0 44 62" role="img" aria-label="Leaf icon">
        <path d="M22 60 C4 48 2 24 10 4 C18 20 22 38 22 60 Z" fill="#5cc043"/>
        <path d="M22 60 C40 48 42 24 34 4 C26 20 22 38 22 60 Z" fill="#5cc043"/>
      </svg>
      <div class="claim-text text-plant">PLANT<br>BASED</div>

      <svg class="claim-icon icon-gelatin" width="60" height="52" viewBox="0 0 60 52" role="img" aria-label="Bone icon">
        <path d="M16 16 C10 2 -2 14 8 22 C-2 32 8 46 16 36 L44 36 C52 46 62 32 52 22 C62 14 50 2 44 16 Z" fill="none" stroke="#5cc043" stroke-width="3" stroke-linejoin="round"/>
      </svg>
      <div class="claim-text text-gelatin">GELATIN<br>FREE</div>
    </div>
  </div>
</div>
</body>
</html>
```